16 Page, A4. Company Brochure. Specialist Travel Company

Design of a 16 Page, A4 brochure for Travel Company specialising in Group Tours for Schools and Sports groups. The brochure should be broken into segments based on the companies subject and destination offerings. The design should inspire people to consider travelling.
Competitor Samples provided for structure and styling.
Text Content will be provided.
Images for use via the below link https://www.filvanta.com/sh/3kqpw8rzenx4m71/BBC2hLoq7TgWzrR9vNk4MeP3xb?dl=0
Target Market(s)
Schools
Industry/Entity Type
Travel
Look and feel

```html
<!DOCTYPE html>
<html lang="en">
<head>
<meta charset="utf-8">
<title>Meridian Group Travel – Sport &amp; Educational Tours Brochure Cover</title>
<link href="https://fonts.googleapis.com/css2?family=Lato:wght@300;400;700;900&family=Roboto+Condensed:wght@300;700&display=swap" rel="stylesheet">
<style>
  :root {
    --backdrop: #d6d6d8;
    --paper: #ffffff;
    --brand-red: #e32b35;
    --fold-red: #b61f2a;
    --photo-light: #e9e4dc;
    --photo-mid: #b9b4ab;
    --photo-cool: #9fb0c2;
    --text-light: #ffffff;
  }
  * { box-sizing: border-box; margin: 0; padding: 0; }
  html, body {
    width: 1200px; height: 900px; overflow: hidden;
    background: var(--backdrop);
  }
  .canvas {
    position: relative; width: 1200px; height: 900px;
    display: flex; align-items: center; justify-content: center;
  }
  .cover {
    position: relative; width: 600px; height: 848px;
    background: var(--paper);
    box-shadow: 0 6px 24px rgba(0,0,0,0.15);
    overflow: hidden;
  }
  .cover-art { position: absolute; inset: 0; width: 100%; height: 100%; }
  .brand-name {
    position: absolute; top: 88px; left: 0; width: 100%;
    text-align: center;
    font-family: "Lato", sans-serif; font-weight: 900;
    font-size: 34px; line-height: 1.0; letter-spacing: 0.5px;
    color: var(--brand-red); text-transform: uppercase;
  }
  .brand-name .brand-mark {
    display: inline-block; width: 14px; height: 14px; border-radius: 50%;
    background: var(--brand-red); margin-right: 10px; vertical-align: middle;
  }
  .tour-title {
    position: absolute; top: 358px; left: 36px;
    font-family: "Roboto Condensed", sans-serif; color: var(--text-light);
    text-transform: uppercase; line-height: 1.0;
  }
  .tour-title .kicker { font-weight: 300; font-size: 30px; letter-spacing: 2px; display: block; }
  .tour-title .headline { font-weight: 700; font-size: 36px; display: block; }
  .company-block {
    position: absolute; top: 672px; left: 62px; width: 330px;
    font-family: "Lato", sans-serif; color: var(--text-light);
  }
  .company-block .company-name { font-weight: 900; font-size: 24px; text-transform: uppercase; line-height: 1.05; }
  .company-block .company-sub { font-weight: 300; font-size: 24px; text-transform: uppercase; line-height: 1.05; }
  .company-block .rule { width: 40px; height: 2px; background: var(--text-light); margin: 12px 0 10px; }
  .company-block .intro { font-size: 9.5px; line-height: 1.45; font-weight: 400; }
  .company-block .web { margin-top: 10px; font-size: 12px; font-weight: 300; letter-spacing: 0.5px; }
</style>
</head>
<body>
<main class="canvas">
  <article class="cover">
    <svg class="cover-art" viewBox="0 0 600 848" preserveAspectRatio="none">
      <defs>
        <linearGradient id="courtPhotoTone" x1="0" y1="0" x2="1" y2="1">
          <stop offset="0" stop-color="var(--photo-cool)"/>
          <stop offset="0.45" stop-color="var(--photo-light)"/>
          <stop offset="1" stop-color="var(--photo-mid)"/>
        </linearGradient>
      </defs>
      <polygon class="hero-photo" role="img" aria-label="Photo of a basketball dropping through a hoop in an indoor gym"
               points="460,190 600,190 600,472 220,472" fill="url(#courtPhotoTone)"/>
      <polygon class="title-band" points="0,320 300,320 460,190 220,472 160,472 0,530" fill="var(--brand-red)"/>
      <polygon class="title-fold" points="300,320 380,255 340,320" fill="var(--fold-red)"/>
      <polygon class="ribbon-fold" points="160,472 340,472 360,500 180,500" fill="var(--fold-red)"/>
      <polygon class="accent-chevron" points="350,472 510,472 430,570" fill="var(--brand-red)"/>
      <polygon class="footer-band" points="0,560 600,640 600,848 0,848" fill="var(--brand-red)"/>
    </svg>

    <h1 class="brand-name"><span class="brand-mark"></span>Meridian<br>Group Travel</h1>

    <h2 class="tour-title">
      <span class="kicker">Sport &amp;</span>
      <span class="headline">Educational</span>
      <span class="headline">Tours</span>
    </h2>

    <section class="company-block">
      <p class="company-name">Meridian</p>
      <p class="company-sub">Group Travel</p>
      <div class="rule"></div>
      <p class="intro">Meridian Group Travel provides the opportunity for Australian school groups and sporting clubs a chance to play matches overseas, enjoy an educational sightseeing program linked to their school studies, attend top level games and visit famous sports venues</p>
      <p class="web">www.meridiangrouptours.com</p>
    </section>
  </article>
</main>
</body>
</html>
```